Clean, creative business Wordpress Site

Our company is building a website via Wordpress and needs a clean, no fuss, modern looking design that reflects our company brand (see attached logos).

In addition, the company is a woman owned business (no middle-aged white guy stock photos please) and primarily works with the oil & gas industry. We would prefer no images with direct references to energy (rigs, windmills, solar panels, etc.). Part of our consulting is providing thought leadership around energy politics and policy so creative ways to incorporate that visually will be appreciated as well.

Site map of pages below:

Home
- About
- Team
- Expertise
- Blog

We prefer a header image that includes the company logo and easy to identify and navigate menus.

Target Market(s)

Energy professionals, Executives

Industry/Entity Type

Consulting

Font styles to use
Serif

Colors
85acd3
0255a3
cedeed
ffffff

Requirements
Must have
• Clean and easy to navigate, clear menus, simple design that reflects company logo.

```html
<!DOCTYPE html>
<html lang="en">
<head>
<meta charset="utf-8">
<title>Corundum Energy</title>
<link href="https://fonts.googleapis.com/css2?family=Raleway:wght@300;400;500;600&family=Arimo:wght@400;700&display=swap" rel="stylesheet">
<style>
:root{
  --blue:#1f5f9c;
  --blue-dark:#17508a;
  --blue-head:#2466a6;
  --blue-soft:#85acd3;
  --blue-pale:#cedeed;
  --white:#ffffff;
  --ink:#333a42;
  --grey:#5b6168;
  --line:#b9c6d3;
  --footer:#1d5e9b;
  --footer-bar:#3f78ae;
  --hero-floor:#e4e6e8;
  --hero-suit:#2b3446;
}
*{margin:0;padding:0;box-sizing:border-box}
html,body{width:1200px;height:3523px;overflow:hidden}
body{font-family:"Arimo",Arial,sans-serif;color:var(--grey);background:var(--white);position:relative}
a{text-decoration:none}
.section{position:absolute;left:0;width:1200px}
.abs{position:absolute}
.heading{font-family:"Raleway",Arial,sans-serif;font-weight:400;letter-spacing:1px}

/* header */
.site-header{top:0;height:113px;background:var(--white);border-top:4px solid var(--blue)}
.brand{left:78px;top:28px;display:flex;align-items:center;gap:14px;font-family:"Raleway",sans-serif;font-weight:600;font-size:34px;color:var(--blue);letter-spacing:1px;white-space:nowrap}
.brand-dot{width:50px;height:50px;border-radius:50%;background:var(--blue)}
.nav{position:absolute;left:517px;top:-4px;height:113px;display:flex;align-items:center;gap:44px}
.nav a{font-family:"Raleway",sans-serif;font-size:15px;font-weight:500;color:var(--ink);line-height:113px;white-space:nowrap}
.nav a.active{background:var(--blue);color:var(--white);width:92px;text-align:center;margin-right:-11px}

/* hero */
.hero{top:113px;height:563px;
  background:
    radial-gradient(ellipse 260px 200px at 28% 38%,rgba(43,52,70,.55),rgba(43,52,70,0) 100%),
    radial-gradient(ellipse 240px 190px at 62% 30%,rgba(43,52,70,.5),rgba(43,52,70,0) 100%),
    radial-gradient(ellipse 200px 220px at 82% 55%,rgba(43,52,70,.4),rgba(43,52,70,0) 100%),
    radial-gradient(ellipse 180px 140px at 12% 70%,rgba(43,52,70,.35),rgba(43,52,70,0) 100%),
    radial-gradient(ellipse 120px 180px at 97% 15%,rgba(190,90,50,.45),rgba(190,90,50,0) 100%),
    linear-gradient(160deg,#cfd2d6 0%,var(--hero-floor) 45%,#c4c7cb 100%)}
.hero-band{left:0;bottom:0;width:1200px;height:77px;background:linear-gradient(90deg,rgba(40,70,110,.2),rgba(30,55,90,.72) 28%,rgba(30,55,90,.72) 72%,rgba(40,70,110,.2));text-align:center;line-height:77px;color:var(--white);font-family:"Raleway",sans-serif;font-size:30px;letter-spacing:1px}

/* divider */
.divider{display:flex;align-items:center;justify-content:center;gap:10px}
.divider span{height:1px;width:110px;background:var(--line)}
.divider i{width:18px;height:18px;border-radius:50%;border:4px solid var(--blue-soft);background:var(--white)}
.divider.light span{background:rgba(255,255,255,.45)}
.divider.left{justify-content:flex-start}

/* welcome */
.welcome{top:676px;height:432px;background:var(--white);text-align:center}
.welcome h1{position:absolute;top:56px;width:100%;font-size:42px;color:var(--blue-head);font-weight:400}
.welcome .divider{position:absolute;top:118px;width:100%}
.welcome p{position:absolute;left:141px;width:918px;font-size:13px;line-height:26px;color:var(--grey)}
.btn{display:inline-block;background:var(--blue);color:var(--white);font-family:"Raleway",sans-serif;font-size:18px;text-align:center;border-radius:3px}
.welcome .btn{position:absolute;left:517px;top:312px;width:166px;height:57px;line-height:57px}

/* services */
.services{top:1108px;height:573px;background:var(--blue);color:var(--white);text-align:center}
.services h2{position:absolute;top:60px;width:100%;font-size:42px;font-weight:400}
.services .divider{position:absolute;top:120px;width:100%}
.service{position:absolute;top:172px;width:250px;margin-left:-125px}
.service-icon{width:150px;height:150px;margin:0 auto;border-radius:50%;border:3px solid rgba(255,255,255,.85);background:rgba(255,255,255,.08);display:flex;align-items:center;justify-content:center}
.service h3{margin-top:48px;font-family:"Raleway",sans-serif;font-weight:400;font-size:17px;line-height:22px;height:44px;display:flex;align-items:center;justify-content:center}
.service p{margin-top:6px;font-size:13px;line-height:23px;color:#e6eef7}

/* about */
.about{top:1681px;height:460px;background:var(--blue-pale)}
.about .kicker{left:78px;top:66px;font-family:"Raleway",sans-serif;font-size:17px;color:var(--ink)}
.about h2{position:absolute;left:78px;top:98px;font-size:40px;color:var(--blue-head);font-weight:400}
.about .divider{position:absolute;left:78px;top:153px;width:520px}
.about .divider span{width:460px}
.about p.intro{position:absolute;left:78px;top:190px;width:640px;font-size:13px;line-height:26px;color:var(--grey)}
.value{position:absolute;top:290px;display:flex;gap:18px}
.value h4{font-family:"Raleway",sans-serif;font-weight:500;font-size:19px;color:var(--blue-head);margin-top:4px}
.value p{margin-top:6px;width:170px;font-size:13px;line-height:25px;color:var(--grey)}
.about-mark{left:800px;top:80px;width:300px;height:300px;border-radius:50%;background:rgba(133,172,211,.35)}

/* team */
.team{top:2141px;height:519px;background:linear-gradient(180deg,#245f98 0%,#1d568f 60%,#1f5c95 100%);color:var(--white);text-align:center}
.team h2{position:absolute;top:55px;width:100%;font-size:42px;font-weight:400}
.team .divider{position:absolute;top:115px;width:100%}
.member-card{left:78px;top:247px;width:246px;height:209px;background:rgba(60,110,160,.55);border:1px solid rgba(255,255,255,.15)}
.member{position:absolute;top:174px;width:260px;margin-left:-130px}
.member-photo{width:146px;height:146px;margin:0 auto;border-radius:50%;border:4px solid var(--white);background:linear-gradient(160deg,#d9d4cf,#9b918a)}
.member h3{margin-top:24px;font-family:"Raleway",sans-serif;font-weight:400;font-size:19px}
.member p{margin-top:8px;font-size:13px;line-height:24px;color:#e6eef7}
.socials{display:flex;justify-content:center;gap:10px;margin-top:8px}
.socials i{width:12px;height:12px;border-radius:50%;background:var(--white)}

/* blog + testimonials */
.lower{top:2660px;height:521px;background:var(--white)}
.lower h2{position:absolute;top:68px;font-size:42px;color:var(--blue-head);font-weight:400}
.lower .divider{position:absolute;top:126px}
.lower .divider span{width:300px}
.col-rule{left:585px;top:40px;width:1px;height:420px;background:#e4e9ee;box-shadow:2px 0 6px rgba(0,0,0,.06)}
.post{position:absolute;left:78px;display:flex;gap:16px}
.post-thumb{width:118px;height:94px;border:3px solid #dfe5eb;background:linear-gradient(150deg,#b8c4cf,#6f8294);flex:none}
.post h3{font-family:"Raleway",sans-serif;font-weight:400;font-size:19px;color:var(--ink)}
.post .date{margin-top:8px;display:flex;align-items:center;gap:8px;font-size:13px;color:var(--blue)}
.post p{margin-top:6px;width:350px;font-size:13px;line-height:23px;color:var(--grey)}
.lower .btn{position:absolute;left:78px;top:404px;width:157px;height:54px;line-height:54px;font-size:19px}
.quote{position:absolute;left:622px;display:flex;gap:22px}
.quote-photo{width:94px;height:94px;border-radius:50%;border:4px solid #e4e9ee;background:linear-gradient(160deg,#d8d0ca,#8e8178);flex:none}
.quote p{width:380px;font-size:13px;line-height:24px;color:var(--grey)}
.quote h4{margin-top:4px;font-weight:700;font-size:14.5px;color:var(--blue-dark)}
.quote-rule{position:absolute;left:670px;height:1px;width:352px;background:var(--line)}
.quote-rule::after{content:"";position:absolute;right:0;top:-4px;width:9px;height:9px;border-radius:50%;background:var(--blue)}

/* footer */
.site-footer{top:3181px;height:275px;background:var(--footer);color:var(--white)}
.site-footer h4{font-family:"Arimo",sans-serif;font-weight:700;font-size:15px;letter-spacing:.5px}
.links{left:78px;top:44px}
.links ul{list-style:none;margin-top:14px}
.links li{font-size:13px;line-height:26px;color:#e6eef7}
.foot-blog{left:329px;top:44px}
.foot-post{display:flex;gap:16px;margin-top:14px}
.foot-post .thumb{width:62px;height:62px;border-radius:50%;border:2px solid var(--white);background:linear-gradient(150deg,#b8c4cf,#6f8294);flex:none}
.foot-post h5{font-weight:400;font-size:13px;margin-top:6px}
.foot-post p{font-size:13px;line-height:22px;color:#e6eef7;width:180px}
.contact{left:629px;top:44px}
.contact-row{display:flex;gap:14px;margin-top:14px;font-size:13px;line-height:22px;color:#e6eef7}
.contact-row svg{flex:none;margin-top:2px}
.foot-brand{left:892px;top:44px;width:230px;text-align:center}
.foot-brand .name{display:flex;align-items:center;justify-content:center;gap:10px;height:90px;font-family:"Raleway",sans-serif;font-weight:600;font-size:17px;color:var(--white);white-space:nowrap}
.foot-brand .name i{width:20px;height:20px;border-radius:50%;background:var(--blue-pale);flex:none}
.foot-brand hr{border:0;height:1px;background:rgba(255,255,255,.45);margin-top:24px}
.foot-brand .circles{display:flex;justify-content:center;gap:14px;margin-top:20px}
.foot-brand .circles i{width:40px;height:40px;border-radius:50%;background:rgba(255,255,255,.3)}
.footer-bar{top:3456px;height:67px;background:var(--footer-bar);color:var(--white);text-align:center;line-height:67px;font-size:14px}
.footer-bar b{font-weight:400;color:#0f4a86}
</style>
</head>
<body>

<header class="section site-header">
  <div class="abs brand"><i class="brand-dot"></i>CORUNDUM ENERGY</div>
  <nav class="nav">
    <a class="active" href="#">HOME</a>
    <a href="#">ABOUT</a>
    <a href="#">TEAM</a>
    <a href="#">EXPERTISE</a>
    <a href="#">BLOG</a>
    <a href="#">CONTACT</a>
  </nav>
</header>

<section class="section hero" role="img" aria-label="Photo of business professionals in dark suits seated in a circle in a bright meeting room, seen from above">
  <div class="abs hero-band">CORUNDUM ENERGY</div>
</section>

<section class="section welcome">
  <h1 class="heading">WELCOME TO CORUNDUM</h1>
  <div class="divider"><span></span><i></i><span></span></div>
  <p style="top:160px">Lorem Ipsum is simply dummy text of the printing and typesetting industry. Lorem Ipsum has been the industry's standard dummy text ever since the 1500s, when an unknown printer took a galley of type and scrambled it to make a type specimen book. It has survived not only five centuries, but also the leap into electronic typesetting, remaining essentially unchanged.</p>
  <p style="top:240px">Lorem Ipsum is simply dummy text of the printing and typesetting industry. Lorem Ipsum has been the industry's standard dummy text ever since the 1500s, when an unknown printer took a galley of type and scrambled it to make a type specimen book.</p>
  <a class="btn" href="#">KNOW MORE</a>
</section>

<section class="section services">
  <h2 class="heading">OUR BEST SERVICES</h2>
  <div class="divider light"><span></span><i></i><span></span></div>

  <div class="service" style="left:204px">
    <div class="service-icon"><svg width="80" height="60" viewBox="0 0 80 60" fill="#fff"><circle cx="20" cy="16" r="8"/><circle cx="40" cy="12" r="9"/><circle cx="60" cy="16" r="8"/><rect x="10" y="28" width="20" height="26" rx="6"/><rect x="29" y="24" width="22" height="30" rx="6"/><rect x="50" y="28" width="20" height="26" rx="6"/></svg></div>
    <h3>COMMUNITY<br>ENGAGEMENT</h3>
    <p>Lorem Ipsum is simply dummy text of the printing and typesetting industry Lorem Ipsum</p>
  </div>
  <div class="service" style="left:470px">
    <div class="service-icon"><svg width="70" height="56" viewBox="0 0 70 56" fill="#fff"><rect x="0" y="0" width="70" height="14" rx="7"/><rect x="0" y="21" width="70" height="14" rx="7"/><rect x="0" y="42" width="70" height="14" rx="7"/></svg></div>
    <h3>NAVIGATING POLICY</h3>
    <p>Lorem Ipsum is simply dummy text of the printing and typesetting industry Lorem Ipsum</p>
  </div>
  <div class="service" style="left:735px">
    <div class="service-icon"><svg width="64" height="72" viewBox="0 0 64 72" fill="none" stroke="#fff" stroke-width="4" stroke-linejoin="round"><path d="M20 70V54C8 48 4 38 6 26 9 10 22 2 36 3c14 1 24 12 24 26l-1 8 4 8-6 2v10c0 4-3 6-7 6h-8v7"/><path d="M34 14l-8 16h10l-6 16" stroke-linecap="round"/></svg></div>
    <h3>DEESCALATING<br>CONFLICT</h3>
    <p>Lorem Ipsum is simply dummy text of the printing and typesetting industry Lorem Ipsum</p>
  </div>
  <div class="service" style="left:1000px">
    <div class="service-icon"><svg width="60" height="76" viewBox="0 0 60 76" fill="#fff"><path d="M30 4a24 24 0 0 0-14 43c3 3 4 6 4 10h20c0-4 1-7 4-10A24 24 0 0 0 30 4z"/><rect x="20" y="61" width="20" height="5" rx="2"/><rect x="22" y="69" width="16" height="5" rx="2"/></svg></div>
    <h3>ENERGY ACCESS</h3>
    <p>Lorem Ipsum is simply dummy text of the printing and typesetting industry Lorem Ipsum</p>
  </div>
</section>

<section class="section about">
  <div class="abs kicker">ABOUT US</div>
  <h2 class="heading">CORUNDUM ENERGY</h2>
  <div class="divider left"><i></i><span></span></div>
  <p class="intro">Lorem Ipsum is simply dummy text of the printing and typesetting industry. Lorem Ipsum has been the industry's standard dummy text ever since the 1500s, when an unknown printer took a galley of type and scrambled it to make a type specimen book.</p>
  <div class="value" style="left:78px">
    <svg width="94" height="94" viewBox="0 0 94 94"><circle cx="47" cy="47" r="42" fill="none" stroke="#1f5f9c" stroke-width="8"/><circle cx="47" cy="47" r="26" fill="none" stroke="#1f5f9c" stroke-width="8"/><circle cx="47" cy="47" r="9" fill="#1f5f9c"/><path d="M47 47L80 14" stroke="#cedeed" stroke-width="8"/><path d="M47 47L80 14" stroke="#1f5f9c" stroke-width="4"/><path d="M72 10h12v12" fill="none" stroke="#1f5f9c" stroke-width="4"/></svg>
    <div><h4>MISSION</h4><p>Lorem Ipsum is simply dummy text of the printing and typesetting industry.</p></div>
  </div>
  <div class="value" style="left:378px">
    <svg width="126" height="94" viewBox="0 0 126 94"><path d="M4 47C24 14 48 6 63 6s39 8 59 41c-20 33-44 41-59 41S24 80 4 47z" fill="none" stroke="#1f5f9c" stroke-width="7"/><circle cx="63" cy="47" r="26" fill="#1f5f9c"/><circle cx="63" cy="47" r="10" fill="#cedeed"/></svg>
    <div><h4>VISSION</h4><p>Lorem Ipsum is simply dummy text of the printing and typesetting industry.</p></div>
  </div>
  <div class="abs about-mark"></div>
</section>

<section class="section team" aria-label="Team section over a soft blue office backdrop">
  <h2 class="heading">OUR TEAM</h2>
  <div class="divider light"><span></span><i></i><span></span></div>
  <div class="abs member-card"></div>
  <div class="member" style="left:202px">
    <div class="member-photo" role="img" aria-label="Portrait of team member"></div>
    <h3>Elsa Varrin</h3>
    <p>Lorem Ipsum is simply dummy<br>text of the printing &amp; type.</p>
    <div class="socials"><i></i><i></i></div>
  </div>
  <div class="member" style="left:467px">
    <div class="member-photo" role="img" aria-label="Portrait of team member"></div>
    <h3>Elsa Varrin</h3>
    <p>Lorem Ipsum is simply dummy<br>text of the printing &amp; type.</p>
    <div class="socials"><i></i><i></i></div>
  </div>
  <div class="member" style="left:737px">
    <div class="member-photo" role="img" aria-label="Portrait of team member"></div>
    <h3>Elsa Varrin</h3>
    <p>Lorem Ipsum is simply dummy<br>text of the printing &amp; type.</p>
    <div class="socials"><i></i><i></i></div>
  </div>
  <div class="member" style="left:1003px">
    <div class="member-photo" role="img" aria-label="Portrait of team member"></div>
    <h3>Elsa Varrin</h3>
    <p>Lorem Ipsum is simply dummy<br>text of the printing &amp; type.</p>
    <div class="socials"><i></i><i></i></div>
  </div>
</section>

<section class="section lower">
  <h2 class="heading" style="left:78px">LATEST BLOG</h2>
  <div class="divider left" style="left:78px"><i></i><span></span></div>

  <div class="post" style="top:176px">
    <div class="post-thumb" role="img" aria-label="Blog photo of colleagues at a meeting table"></div>
    <div>
      <h3>Lorem Ipsum is simply dummy text.</h3>
      <div class="date"><svg width="14" height="14" viewBox="0 0 14 14"><rect x="1" y="2" width="12" height="11" fill="none" stroke="#1f5f9c" stroke-width="1.5"/><rect x="1" y="2" width="12" height="3" fill="#1f5f9c"/></svg>28 Dec 2016</div>
      <p>Lorem Ipsum is simply dummy text of the printing and typesetting industry. Lorem Ipsum has been the</p>
    </div>
  </div>
  <div class="post" style="top:294px">
    <div class="post-thumb" role="img" aria-label="Blog photo of a business presentation"></div>
    <div>
      <h3>Lorem Ipsum is simply dummy text.</h3>
      <div class="date"><svg width="14" height="14" viewBox="0 0 14 14"><rect x="1" y="2" width="12" height="11" fill="none" stroke="#1f5f9c" stroke-width="1.5"/><rect x="1" y="2" width="12" height="3" fill="#1f5f9c"/></svg>28 Dec 2016</div>
      <p>Lorem Ipsum is simply dummy text of the printing and typesetting industry. Lorem Ipsum has been the</p>
    </div>
  </div>
  <a class="btn" href="#">VIEW ALL</a>

  <div class="abs col-rule"></div>

  <h2 class="heading" style="left:622px">TESTIMONIALS</h2>
  <div class="divider left" style="left:622px"><i></i><span></span></div>

  <div class="quote" style="top:162px">
    <div class="quote-photo" role="img" aria-label="Client portrait"></div>
    <div><p>" Lorem Ipsum is simply dummy text of the printing and typesetting industry. Lorem Ipsum has been the industry's standard dummy text ever since the 1500s"</p><h4>—Client Name</h4></div>
  </div>
  <div class="quote-rule" style="top:276px"></div>
  <div class="quote" style="top:302px">
    <div class="quote-photo" role="img" aria-label="Client portrait"></div>
    <div><p>" Lorem Ipsum is simply dummy text of the printing and typesetting industry. Lorem Ipsum has been the industry's standard dummy text ever since the 1500s"</p><h4>—Client Name</h4></div>
  </div>
  <div class="quote-rule" style="top:416px"></div>
</section>

<footer class="section site-footer">
  <div class="abs links">
    <h4>USEFUL LINKS</h4>
    <ul><li>» Home</li><li>» About</li><li>» Team</li><li>» Expertise</li><li>» Blog</li><li>» Contact</li></ul>
  </div>
  <div class="abs foot-blog">
    <h4>LATEST BLOG</h4>
    <div class="foot-post"><div class="thumb" role="img" aria-label="Blog thumbnail"></div><div><h5>BLOG TITLE</h5><p>Lorem Ipsum is the simply dummy text of the ...</p></div></div>
    <div class="foot-post"><div class="thumb" role="img" aria-label="Blog thumbnail"></div><div><h5>BLOG TITLE</h5><p>Lorem Ipsum is the simply dummy text of the ...</p></div></div>
  </div>
  <div class="abs contact">
    <h4>GET IN TOUCH</h4>
    <div class="contact-row"><svg width="18" height="22" viewBox="0 0 18 22"><path d="M9 1a7 7 0 0 0-7 7c0 5 7 13 7 13s7-8 7-13a7 7 0 0 0-7-7z" fill="none" stroke="#fff" stroke-width="1.6"/><circle cx="9" cy="8" r="2.5" fill="none" stroke="#fff" stroke-width="1.6"/></svg><div>CORUNDUM ENERGY<br>Lorem Ipsum is simple text of<br>print text of type setting.</div></div>
    <div class="contact-row"><svg width="18" height="18" viewBox="0 0 18 18"><path d="M4 1l3 4-2 2c1 3 3 5 6 6l2-2 4 3-2 3C8 17 1 10 1 3z" fill="none" stroke="#fff" stroke-width="1.6"/></svg><div>123 456 7890</div></div>
    <div class="contact-row"><svg width="18" height="18" viewBox="0 0 18 18"><rect x="4" y="1" width="10" height="5" fill="none" stroke="#fff" stroke-width="1.6"/><rect x="1" y="6" width="16" height="7" fill="none" stroke="#fff" stroke-width="1.6"/><rect x="4" y="11" width="10" height="6" fill="none" stroke="#fff" stroke-width="1.6"/></svg><div>123 456 7890</div></div>
    <div class="contact-row"><svg width="18" height="14" viewBox="0 0 18 14"><rect x="1" y="1" width="16" height="12" fill="none" stroke="#fff" stroke-width="1.6"/><path d="M1 1l8 7 8-7" fill="none" stroke="#fff" stroke-width="1.6"/></svg><div>info@corundumenergy.com</div></div>
  </div>
  <div class="abs foot-brand">
    <div class="name"><i></i>CORUNDUM ENERGY</div>
    <hr>
    <div class="circles"><i></i><i></i><i></i></div>
  </div>
</footer>

<div class="section footer-bar">© 2016 <b>CORUNDUM ENERGY</b> . All rights reserved.</div>

</body>
</html>
```